Yard Sign Design Needed

Yard sign needed for mowing & landscaping company. Would like to use the top logo with black background which is attached. Would like MOWING to be in large standout letters. The word "landscaping" can be smaller and more artistic or omitted. Will need room for phone number once design is approved. The phone number will need to stand out and look identical/similar to the word 'MOWING"

```html
<!DOCTYPE html>
<html lang="en">
<head>
<meta charset="utf-8">
<title>Norvale Contractors – Mowing Yard Sign</title>
<link rel="stylesheet" href="https://fonts.googleapis.com/css2?family=Barlow:wght@700;800&display=swap">
<style>
  :root {
    --page-bg: #eef0ea;
    --sign-edge: #ffffff;
    --brand-green: #8ca63b;
    --panel-black: #050505;
    --logo-black: #0b0b0c;
    --text-white: #ffffff;
  }
  * { margin: 0; padding: 0; box-sizing: border-box; }
  html, body {
    width: 1200px;
    height: 967px;
    overflow: hidden;
    background: var(--page-bg);
    font-family: "Barlow", Arial, sans-serif;
  }
  .yard-sign {
    position: absolute;
    left: 50px;
    top: 55px;
    width: 1100px;
    height: 856px;
    background: var(--brand-green);
    border: 3px solid var(--sign-edge);
  }
  .sign-panel {
    position: absolute;
    left: 49px;
    top: 53px;
    right: 49px;
    bottom: 54px;
    background: var(--panel-black);
    border-radius: 26px;
  }
  .service-secondary {
    position: absolute;
    top: 117px;
    left: 0;
    width: 100%;
    text-align: center;
    color: var(--text-white);
    font-weight: 800;
    font-size: 58px;
    letter-spacing: 2px;
    line-height: 1;
  }
  .service-primary {
    position: absolute;
    top: 170px;
    left: 0;
    width: 100%;
    text-align: center;
    color: var(--brand-green);
    font-weight: 800;
    font-size: 200px;
    letter-spacing: 4px;
    line-height: 1;
  }
  .company-block {
    position: absolute;
    left: 136px;
    top: 352px;
    width: 752px;
    height: 236px;
    background: var(--logo-black);
    display: flex;
    align-items: center;
    justify-content: center;
    gap: 34px;
  }
  .company-mark {
    width: 92px;
    height: 92px;
    background: var(--brand-green);
  }
  .company-name {
    color: var(--brand-green);
    font-weight: 700;
    line-height: 1.05;
  }
  .company-name .name-main {
    display: block;
    font-size: 84px;
    letter-spacing: 3px;
  }
  .company-name .name-sub {
    display: block;
    font-size: 38px;
    letter-spacing: 2px;
  }
  .phone-number {
    position: absolute;
    top: 590px;
    left: 0;
    width: 100%;
    text-align: center;
    color: var(--text-white);
    font-weight: 800;
    font-size: 134px;
    letter-spacing: 3px;
    line-height: 1;
  }
</style>
</head>
<body>
  <div class="yard-sign">
    <div class="sign-panel">
      <p class="service-secondary">LANDSCAPING</p>
      <p class="service-primary">MOWING</p>
      <div class="company-block">
        <span class="company-mark"></span>
        <p class="company-name">
          <span class="name-main">NORVALE</span>
          <span class="name-sub">CONTRACTORS LLC</span>
        </p>
      </div>
      <p class="phone-number">+12 555 0148</p>
    </div>
  </div>
</body>
</html>
```